Bref créative
Saltmarsh Restaurant
Truly Island-Made
Simple
#41 Estate Coralind
(at the Harbor Bluff Cottages)
Palmetto Cay, VI 00899
Saltmarsh_Restaurant@bayvistamail.com
www.saltmarshvi-example.com
* Free Wi-fi
* Special events venue-mediations, meetings, fund raisers, wedding receptions, catering, private parties, you name it we can host it !!
* Superior customer service
* Delicious cuisine
please use this logo

```html
<!DOCTYPE html>
<html lang="en">
<head>
<meta charset="utf-8">
<title>Saltmarsh Restaurant Stationery</title>
<link href="https://fonts.googleapis.com/css2?family=Cormorant+Garamond:wght@500;600&family=Lato:wght@400;700&display=swap" rel="stylesheet">
<style>
:root{
  --backdrop:#ebebeb;
  --paper:#ffffff;
  --teal:#7cc6bd;
  --teal-light:#c9ebe5;
  --gold:#d8b46a;
  --orange:#e39a4b;
  --ink:#333333;
  --rule:#8a8a8a;
  --cell:#dcdcdc;
}
*{box-sizing:border-box;margin:0;padding:0}
html,body{width:1200px;height:552px;overflow:hidden;background:var(--backdrop)}
body{position:relative;font-family:"Lato",Arial,sans-serif;color:var(--ink)}
.sheet{position:absolute;background:var(--paper);box-shadow:0 1px 3px rgba(0,0,0,.18);overflow:hidden}
.fax-sheet{left:19px;top:14px;width:365px;height:519px}
.letterhead{left:403px;top:14px;width:360px;height:519px}
.card-front{left:775px;top:24px;width:156px;height:91px}
.card-back{left:946px;top:24px;width:153px;height:91px}
.envelope-wide{left:775px;top:130px;width:324px;height:184px}
.envelope-flat{left:775px;top:336px;width:324px;height:197px}
.corner{position:absolute;width:100%;height:100%;left:0;top:0}
.watermark{position:absolute;border-radius:50%;background:radial-gradient(circle,rgba(124,198,189,.16),rgba(124,198,189,0) 70%)}
.brand{position:absolute;display:flex;align-items:center;gap:4px}
.brand-dot{width:7px;height:7px;border-radius:50%;background:var(--teal)}
.brand-name{font-family:"Cormorant Garamond",Georgia,serif;font-weight:600;color:var(--teal);font-size:20px;line-height:1}
.contact{position:absolute;font-size:4.6px;line-height:6.2px;color:var(--orange);white-space:nowrap}
.fax-title{position:absolute;right:24px;top:130px;font-size:8px;font-weight:700;letter-spacing:.5px}
.fax-table{position:absolute;left:34px;top:145px;width:307px;border-collapse:collapse;font-size:5.5px}
.fax-table td{border:1px solid var(--rule);height:19px;padding:0 3px}
.fax-table .label{background:var(--cell);width:30px}
.fax-checks{position:absolute;left:34px;top:231px;display:flex;gap:17px;font-size:5px}
.fax-checks span{display:flex;align-items:center;gap:3px}
.fax-checks i{width:6px;height:6px;border:1px solid var(--rule);display:inline-block}
</style>
</head>
<body>

<section class="sheet fax-sheet">
  <div class="watermark" role="img" aria-label="Faint floral motif" style="left:170px;top:390px;width:190px;height:150px"></div>
  <svg class="corner" viewBox="0 0 365 519" preserveAspectRatio="none">
    <defs><linearGradient id="tealFax" x1="0" y1="1" x2="1" y2="0"><stop offset="0" stop-color="var(--teal)"/><stop offset="1" stop-color="var(--teal-light)"/></linearGradient></defs>
    <path d="M0 519 L0 440 Q10 505 80 519 Z" fill="url(#tealFax)"/>
    <path d="M0 430 Q12 510 100 519" fill="none" stroke="var(--gold)" stroke-width="1"/>
    <path d="M300 0 Q330 20 365 24" fill="none" stroke="var(--gold)" stroke-width=".8"/>
  </svg>
  <div class="brand" style="left:16px;top:12px"><span class="brand-dot"></span><span class="brand-name">Saltmarsh</span></div>
  <div class="contact" style="left:16px;top:36px">#41 Estate Coralind (at the Harbor Bluff Cottages)<br>Palmetto Cay, VI 00899<br>Tel 340 555 0142<br>Saltmarsh_Restaurant@bayvistamail.com<br>www.saltmarshvi-example.com</div>
  <div class="fax-title">FAX</div>
  <table class="fax-table">
    <tr><td class="label">To:</td><td></td><td class="label">From:</td><td></td></tr>
    <tr><td class="label">Fax:</td><td></td><td class="label">Pages:</td><td></td></tr>
    <tr><td class="label">Phone:</td><td></td><td class="label">Date:</td><td></td></tr>
    <tr><td class="label">Re:</td><td></td><td class="label">CC:</td><td></td></tr>
  </table>
  <div class="fax-checks">
    <span><i></i>Urgent</span><span><i></i>For Review</span><span><i></i>Please Comment</span><span><i></i>Please Reply</span><span><i></i>Please Recycle</span>
  </div>
</section>

<section class="sheet letterhead">
  <div class="watermark" role="img" aria-label="Faint floral motif" style="left:175px;top:380px;width:190px;height:150px"></div>
  <svg class="corner" viewBox="0 0 360 519" preserveAspectRatio="none">
    <defs><linearGradient id="tealLetter" x1="1" y1="1" x2="0" y2="0"><stop offset="0" stop-color="var(--teal)"/><stop offset="1" stop-color="var(--teal-light)"/></linearGradient></defs>
    <path d="M360 519 L360 440 Q350 505 280 519 Z" fill="url(#tealLetter)"/>
    <path d="M360 430 Q348 510 260 519" fill="none" stroke="var(--gold)" stroke-width="1"/>
  </svg>
  <div class="brand" style="left:16px;top:12px"><span class="brand-dot"></span><span class="brand-name">Saltmarsh</span></div>
  <div class="contact" style="left:16px;top:36px">#41 Estate Coralind (at the Harbor Bluff Cottages)<br>Palmetto Cay, VI 00899<br>Tel 340 555 0142<br>Saltmarsh_Restaurant@bayvistamail.com<br>www.saltmarshvi-example.com</div>
</section>

<section class="sheet card-front">
  <svg class="corner" viewBox="0 0 156 91" preserveAspectRatio="none">
    <path d="M156 91 L156 66 Q150 88 126 91 Z" fill="var(--teal)" opacity=".7"/>
    <path d="M156 60 Q150 89 118 91" fill="none" stroke="var(--gold)" stroke-width=".7"/>
  </svg>
  <div class="brand" style="left:26px;top:9px"><span class="brand-dot" style="width:5px;height:5px"></span><span class="brand-name" style="font-size:13px">Saltmarsh</span></div>
  <div class="contact" style="left:26px;top:26px;font-size:3.6px;line-height:4.8px">Truly Island-Made<br>#41 Estate Coralind<br>Palmetto Cay, VI 00899<br>Saltmarsh_Restaurant@bayvistamail.com<br>www.saltmarshvi-example.com</div>
</section>

<section class="sheet card-back">
  <svg class="corner" viewBox="0 0 153 91" preserveAspectRatio="none">
    <path d="M153 91 L153 66 Q147 88 123 91 Z" fill="var(--teal)" opacity=".7"/>
    <path d="M153 60 Q147 89 115 91" fill="none" stroke="var(--gold)" stroke-width=".7"/>
  </svg>
  <div class="contact" style="left:12px;top:30px;font-size:3.8px;line-height:5px">Free Wi-fi &middot; Special events venue<br>Superior customer service<br>Delicious cuisine<br>Saltmarsh_Restaurant@bayvistamail.com</div>
</section>

<section class="sheet envelope-wide">
  <div class="watermark" role="img" aria-label="Faint floral motif" style="left:130px;top:10px;width:180px;height:160px"></div>
  <svg class="corner" viewBox="0 0 324 184" preserveAspectRatio="none">
    <path d="M0 184 L0 140 Q6 178 48 184 Z" fill="var(--teal)" opacity=".75"/>
    <path d="M0 130 Q8 180 62 184" fill="none" stroke="var(--gold)" stroke-width=".8"/>
  </svg>
  <div class="brand" style="left:14px;top:12px"><span class="brand-dot" style="width:6px;height:6px"></span><span class="brand-name" style="font-size:17px">Saltmarsh</span></div>
  <div class="contact" style="left:14px;top:33px;font-size:4.2px;line-height:5.6px">#41 Estate Coralind<br>Palmetto Cay, VI 00899<br>Tel 340 555 0142<br>www.saltmarshvi-example.com</div>
</section>

<section class="sheet envelope-flat">
  <svg class="corner" viewBox="0 0 324 197" preserveAspectRatio="none">
    <path d="M0 0 L0 40 Q6 8 48 0 Z" fill="var(--teal)" opacity=".75"/>
    <path d="M0 52 Q8 6 62 0" fill="none" stroke="var(--gold)" stroke-width=".8"/>
  </svg>
  <div class="brand" style="left:50%;top:34px;transform:translateX(-50%)"><span class="brand-dot" style="width:6px;height:6px"></span><span class="brand-name" style="font-size:17px">Saltmarsh</span></div>
</section>

</body>
</html>
```